Business card design for QuelMarvion

I need a business card based on the logo design produced for QuelMarvion. The company is focused on triathlon and endurance sport coaching and the tag line is (per the logo) "Discipline. Balance. Performance". The design should be sophisticated, appropriate to an affluent and business oriented target market. Colors are optional but the color of the logo probably dictates the color used on the card. I envisage using the red logo, with black print for the wording and contact numbers on a white or cream background, but am open to alternative suggestions. I expect to select something fairly conventional, but would like to see some designs that are less conventional to stretch my thinking on what could be appropriate. I am assuming a single side design is best, but willing to consider double sided as an option.

Target Market(s)

Individual athletes and corporate health and wellness leaders

Industry/Entity Type

Health And Wellness

Contact Information for Business Card

The card should provide the following information:
Logo
My name: Gordon Lashby
Company website: QuelMarvion.com
My email: gordon.lashby@quelmarvion.com
My cell phone number: +1-555-018-2739

Font styles to use
Sans Serif

Colors

Designer to choose colors to be used in the design.

Requirements
Must have
• Space on the card - simple design, not over crowded.
Nice to have
• clean and clear font, nothing garish or mass market like
Should not have
• Do not add pictures

```html
<!DOCTYPE html>
<html lang="en">
<head>
<meta charset="utf-8">
<title>QuelMarvion Business Card</title>
<link href="https://fonts.googleapis.com/css2?family=Lato:wght@400;700&display=swap" rel="stylesheet">
<style>
  :root {
    --stage: #555555;
    --card-white: #ffffff;
    --card-black: #050505;
    --pattern-tone: #1a1a1a;
    --brand-red: #b0252a;
    --ink: #1a1a1a;
    --rule: #9a9a9a;
  }
  html, body {
    margin: 0;
    padding: 0;
    width: 1200px;
    height: 900px;
    overflow: hidden;
    background: var(--stage);
    font-family: "Lato", sans-serif;
  }
  .canvas {
    position: relative;
    width: 1200px;
    height: 900px;
  }
  .card {
    position: absolute;
    top: 170px;
    width: 347px;
    height: 561px;
    box-shadow: 3px 4px 6px rgba(0,0,0,0.45);
    overflow: hidden;
  }
  .card-front {
    left: 259px;
    background: var(--card-white);
    text-align: center;
  }
  .card-back {
    left: 631px;
    background: var(--card-black);
  }
  .brand-name {
    position: absolute;
    left: 0;
    right: 0;
    margin: 0;
    color: var(--brand-red);
    font-weight: 700;
    letter-spacing: 0.5px;
    text-align: center;
    line-height: 1;
  }
  .card-front .brand-name {
    top: 156px;
    font-size: 44px;
  }
  .tagline {
    position: absolute;
    top: 200px;
    left: 0;
    right: 0;
    margin: 0;
    font-size: 14px;
    color: var(--ink);
    letter-spacing: 0.3px;
  }
  .holder-name {
    position: absolute;
    top: 390px;
    left: 0;
    right: 0;
    margin: 0;
    font-size: 20px;
    font-weight: 400;
    color: var(--brand-red);
    letter-spacing: 0.3px;
  }
  .divider {
    position: absolute;
    top: 430px;
    left: 59px;
    width: 228px;
    height: 1px;
    background: var(--rule);
  }
  .contact-list {
    position: absolute;
    top: 448px;
    left: 0;
    right: 0;
    margin: 0;
    padding: 0;
    list-style: none;
    font-size: 16px;
    line-height: 20px;
    color: var(--ink);
  }
  .contact-label, .contact-web {
    color: var(--brand-red);
  }
  .back-pattern {
    position: absolute;
    inset: 0;
    background: radial-gradient(ellipse at 50% 50%, var(--pattern-tone) 0%, var(--card-black) 75%);
  }
  .card-back .brand-name {
    top: 284px;
    font-size: 44px;
  }
</style>
</head>
<body>
<div class="canvas">
  <section class="card card-front">
    <p class="brand-name">QuelMarvion</p>
    <p class="tagline">DISCIPLINE. BALANCE. PERFORMANCE</p>
    <h1 class="holder-name">GORDON LASHBY</h1>
    <div class="divider"></div>
    <ul class="contact-list">
      <li><span class="contact-label">P:</span> +1-555-018-2739</li>
      <li class="contact-web">www.QuelMarvion.com</li>
      <li><span class="contact-label">E:</span> gordon.lashby@quelmarvion.com</li>
    </ul>
  </section>
  <section class="card card-back">
    <div class="back-pattern" role="img" aria-label="Faint dark repeating pattern of athletic figure shapes"></div>
    <p class="brand-name">QuelMarvion</p>
  </section>
</div>
</body>
</html>
```